Flyer for Pharmacy/Medical Convention

Tri-fold flyer for pharmacy/medical convention. The inside of the flyer we would like to look like a venn diagram, possibly using an image similar to our blue logo

Copy write will be submitted when a design is chosen

there will be a flap about educational features, one about supplements an automated recommendations, and a flap about a computer platform to manage patients

Target Market(s)

Pharmacists and Medical Providers

Industry/Entity Type

Supplement

Colors

Designer to choose colors to be used in the design.

Requirements
Must have
• color scheme similar to logos and or label design attached

```html
<!DOCTYPE html>
<html lang="en">
<head>
<meta charset="UTF-8">
<title>Convention Flyer – Inside Spread</title>
<link href="https://fonts.googleapis.com/css2?family=Lato:wght@400;700;900&display=swap" rel="stylesheet">
<style>
  :root {
    --backdrop: #5cb4e6;
    --page-indigo: #6c74cc;
    --circle-deep: #4c55bb;
    --circle-sky: #4a9ad8;
    --circle-teal: #3fc6b8;
    --page-paper: #f2f3f5;
    --text-light: #ffffff;
    --photo-grey-a: #d9dadc;
    --photo-grey-b: #9a9b9e;
    --photo-lab-a: #dfe9f2;
    --photo-lab-b: #7e9bb8;
    --product-dark-a: #2b2f3a;
    --product-dark-b: #11131a;
  }
  * { margin: 0; padding: 0; box-sizing: border-box; }
  html, body {
    width: 1200px;
    height: 900px;
    overflow: hidden;
    background: var(--backdrop);
    font-family: "Lato", sans-serif;
  }
  .spread {
    position: absolute;
    left: 100px;
    top: 110px;
    width: 1000px;
    height: 680px;
    box-shadow: 0 20px 50px rgba(20, 60, 110, 0.25);
  }
  .spread-art {
    position: absolute;
    inset: 0;
    width: 1000px;
    height: 680px;
    display: block;
  }
  .intro-copy {
    position: absolute;
    left: 255px;
    top: 62px;
    width: 225px;
    color: var(--text-light);
  }
  .intro-title {
    font-weight: 900;
    font-size: 23px;
    line-height: 1.05;
  }
  .intro-subtitle {
    font-weight: 700;
    font-size: 17px;
    line-height: 1.2;
    margin-bottom: 12px;
  }
  .intro-body {
    font-weight: 400;
    font-size: 14px;
    line-height: 1.45;
  }
</style>
</head>
<body>
  <main class="spread">
    <svg class="spread-art" viewBox="0 0 1000 680" xmlns="http://www.w3.org/2000/svg">
      <defs>
        <clipPath id="spread-clip"><rect x="0" y="0" width="1000" height="680"/></clipPath>
        <linearGradient id="portrait-tone" x1="0" y1="0" x2="1" y2="1">
          <stop offset="0" stop-color="var(--photo-grey-a)"/>
          <stop offset="1" stop-color="var(--photo-grey-b)"/>
        </linearGradient>
        <linearGradient id="lab-tone" x1="0" y1="0" x2="1" y2="1">
          <stop offset="0" stop-color="var(--photo-lab-a)"/>
          <stop offset="1" stop-color="var(--photo-lab-b)"/>
        </linearGradient>
        <linearGradient id="product-tone" x1="0" y1="0" x2="1" y2="1">
          <stop offset="0" stop-color="var(--product-dark-a)"/>
          <stop offset="1" stop-color="var(--product-dark-b)"/>
        </linearGradient>
        <linearGradient id="fold-shade" x1="0" y1="0" x2="1" y2="0">
          <stop offset="0" stop-color="#000" stop-opacity="0"/>
          <stop offset="0.5" stop-color="#000" stop-opacity="0.12"/>
          <stop offset="1" stop-color="#000" stop-opacity="0"/>
        </linearGradient>
      </defs>
      <g clip-path="url(#spread-clip)">
        <rect class="page-left" x="0" y="0" width="500" height="680" fill="var(--page-indigo)"/>
        <rect class="page-right" x="500" y="0" width="500" height="680" fill="var(--page-paper)"/>
        <rect class="portrait-photo" x="620" y="0" width="380" height="360" fill="url(#portrait-tone)"
              role="img" aria-label="Greyscale photo of a senior pharmacist examining a sample"/>
        <circle class="venn-deep" cx="170" cy="360" r="300" fill="var(--circle-deep)"/>
        <circle class="venn-sky" cx="420" cy="540" r="260" fill="var(--circle-sky)" opacity="0.8"/>
        <circle class="venn-teal" cx="570" cy="330" r="230" fill="var(--circle-teal)" opacity="0.75"/>
        <rect class="product-photo" x="70" y="300" width="200" height="190" rx="14" fill="url(#product-tone)"
              role="img" aria-label="Photo of supplement tubs"/>
        <circle class="lab-photo-large" cx="740" cy="390" r="112" fill="url(#lab-tone)"
                stroke="#ffffff" stroke-width="9"
                role="img" aria-label="Photo of a scientist working with test tubes in a laboratory"/>
        <circle class="lab-photo-small" cx="575" cy="565" r="76" fill="url(#lab-tone)"
                stroke="#ffffff" stroke-width="8"
                role="img" aria-label="Photo of a researcher using a microscope"/>
        <rect class="fold" x="485" y="0" width="30" height="680" fill="url(#fold-shade)"/>
      </g>
    </svg>

    <section class="intro-copy">
      <h1 class="intro-title">Lorem ipsum dolor</h1>
      <h2 class="intro-subtitle">Sit amet, consectetur</h2>
      <p class="intro-body">Interdum et malesuada fames ac ante ipsum primis in faucibus. Curabitur venenatis tristique ipsum. Cras sollicitudin lectus sem, id tempus sapien posuere at. Proin ac elementum ante. Mauris ut metus ut metus vehicula cursus et non ipsum. Cras ullamcorper pellentesque nisl, vitae dictum urna fringilla vitae.</p>
    </section>
  </main>
</body>
</html>
```